Healthcare technology company website - Tralom

Create wireframe design for Tralom, an Australian based medical technology company developing a robotic ultrasound system.

Current site tralom.com
https://www.plandeck.example/proto/k7pLwQ2zR9dXmB4nC8vT5E/Tralom-Website?node-id=2210-3381&t=aBcDeFgHiJkLmNoP-1.
https://www.plandeck.example/proto/k7pLwQ2zR9dXmB4nC8vT5E/Tralom-Website?page-id=2207%3A518&node-id=2233-4410&viewport=-33%2C513%2C0.15&t=QrStUvWxYzAbCdEf-1&scaling=min-zoom&content-scaling=fixed&starting-point-node-id=2233%3A4410
The attached mp4 to be the hero view. Open to designer who can improve it. Attached figma

Industry/Entity Type

tech healthcare

Number of Pages Required

4 page

Requirements
Must have
• Hero view with mp4 attached. Hardware interaction model similar to https://www.quorvin.example/au/sonebuds-4/ div class="section section-redesigned no-pad-bottom will-change"

```html
<!DOCTYPE html>
<html lang="en">
<head>
<meta charset="utf-8">
<title>Tralom — Vascular Imaging, Reimagined</title>
<link rel="stylesheet" href="https://fonts.googleapis.com/css2?family=Plus+Jakarta+Sans:wght@300;400;500;600;700;800&display=swap">
<style>
  :root {
    --ink: #0a0a0a;
    --paper: #ffffff;
    --muted: #b9b9bd;
    --body: #2a2a2e;
    --violet: #8f0ad6;
    --magenta: #e0148f;
    --pink: #f2207a;
    --card: #f9f7f8;
    --card-line: #ece8ec;
    --rule: #cfcfd3;
  }
  * { box-sizing: border-box; margin: 0; padding: 0; }
  html, body { width: 1200px; height: 3229px; overflow: hidden; background: var(--paper); }
  body { position: relative; font-family: "Plus Jakarta Sans", sans-serif; color: var(--ink); }
  .abs { position: absolute; }

  .brand { font-family: "Plus Jakarta Sans", sans-serif; font-weight: 300; color: var(--ink); letter-spacing: 1px; }
  .site-header .brand { left: 58px; top: 34px; font-size: 40px; line-height: 46px; }
  .nav { display: flex; font-size: 16px; font-weight: 500; }
  .nav a { position: absolute; color: var(--ink); text-decoration: none; white-space: nowrap; }
  .btn {
    position: absolute; display: flex; align-items: center; justify-content: space-between;
    background: var(--ink); color: var(--paper); border-radius: 20px;
    font-size: 18px; font-weight: 500; padding: 0 22px; text-decoration: none;
  }
  .btn svg { width: 14px; height: 14px; }

  .hero-brand { left: 0; width: 1200px; top: 180px; text-align: center; font-size: 130px; line-height: 150px; }
  .play {
    left: 562px; top: 321px; width: 52px; height: 52px; border-radius: 50%;
    background: var(--paper); border: 1px solid #e4e4e8; display: flex; align-items: center; justify-content: center;
  }
  .hero-title {
    left: 0; width: 1200px; top: 380px; text-align: center; font-size: 70px; font-weight: 600; line-height: 84px; letter-spacing: -1px;
    background: linear-gradient(90deg, var(--violet), var(--magenta) 70%, #ee2a6f);
    -webkit-background-clip: text; background-clip: text; color: transparent;
  }
  .hero-haze { left: 0; top: 420px; width: 1200px; height: 320px;
    background: radial-gradient(ellipse at 30% 40%, rgba(150,190,230,.18), transparent 60%); }

  .partner { top: 602px; height: 179px; background: var(--card); border: 1px solid var(--card-line); border-radius: 6px; }
  .partner span { position: absolute; left: 50%; top: 50%; width: 150px; height: 32px; margin: -16px 0 0 -75px; background: #dcd8de; border-radius: 4px; }

  .pill {
    position: absolute; height: 37px; border: 1.5px solid var(--ink); border-radius: 19px;
    color: var(--violet); font-size: 18px; font-weight: 500; display: flex; align-items: center; justify-content: center;
  }
  .section-title { font-size: 88px; font-weight: 800; line-height: 100px; letter-spacing: -1px; }
  .section-lede { font-size: 30px; font-weight: 600; line-height: 36px; color: var(--muted); letter-spacing: -.3px; }
  .section-body { font-size: 20px; line-height: 28px; color: var(--body); }
  .media { border-radius: 8px; }
</style>
</head>
<body>

<header class="site-header">
  <div class="abs brand">Tralom</div>
  <nav class="nav">
    <a style="left:431px;top:48px">Home</a>
    <a style="left:515px;top:48px">About</a>
    <a style="left:602px;top:48px">Technology</a>
    <a style="left:734px;top:48px">Work with us</a>
  </nav>
  <a class="btn" style="left:1034px;top:40px;width:108px;height:36px;font-size:17px;justify-content:center;padding:0">Contact</a>
</header>

<section class="hero">
  <div class="abs hero-haze"></div>
  <div class="abs brand hero-brand">Tralom</div>
  <div class="abs play">
    <svg width="16" height="16" viewBox="0 0 16 16"><path d="M4 2 L14 8 L4 14 Z" fill="#0a0a0a"/></svg>
  </div>
  <h1 class="abs hero-title">Vascular Imaging, Reimagined</h1>
</section>

<section class="partners" aria-label="Partners">
  <div class="abs partner" style="left:55px;width:262px"><span></span></div>
  <div class="abs partner" style="left:330px;width:262px"><span></span></div>
  <div class="abs partner" style="left:604px;width:264px"><span></span></div>
  <div class="abs partner" style="left:879px;width:263px"><span></span></div>
</section>

<section class="mission">
  <div class="abs media" role="img" aria-label="Bright lavender clinic room with examination table, desk and laptop"
       style="left:58px;top:890px;width:540px;height:432px;background:linear-gradient(160deg,#b8b3e6,#d9d6ee 55%,#c9c6cf)"></div>
  <div class="pill" style="left:651px;top:890px;width:125px">About</div>
  <h2 class="abs section-title" style="left:648px;top:938px">Mission</h2>
  <p class="abs section-lede" style="left:651px;top:1051px;width:500px">Developing the next generation of Vascular Imaging Solutions</p>
  <p class="abs section-body" style="left:651px;top:1141px;width:500px">Tralom is a Medical Imaging, Deep Learning and Robotics Company on a mission to improve lives by Developing the next generation of Vascular Imaging Solutions</p>
  <a class="btn" style="left:644px;top:1285px;width:180px;height:37px">Learn More
    <svg viewBox="0 0 14 14"><path d="M2 12 L12 2 M5 2 H12 V9" stroke="#fff" stroke-width="1.5" fill="none"/></svg></a>
</section>

<section class="software">
  <div class="pill" style="left:56px;top:1524px;width:126px">Product</div>
  <h2 class="abs section-title" style="left:56px;top:1572px">Software</h2>
  <p class="abs section-lede" style="left:58px;top:1687px;width:520px">Monitoring vascular access health through automated 3D imaging at the point of care.</p>
  <p class="abs section-body" style="left:56px;top:1821px;width:530px">Tralom completes the scan in minutes, pre-populating a report with an accurate 3D digital twin of the patient’s vasculature.</p>
  <a class="btn" style="left:56px;top:1933px;width:180px;height:37px">Learn More
    <svg viewBox="0 0 14 14"><path d="M2 12 L12 2 M5 2 H12 V9" stroke="#fff" stroke-width="1.5" fill="none"/></svg></a>
  <div class="abs media" role="img" aria-label="Rendered red blood vessel showing disease progression over time, on a dark navy background"
       style="left:603px;top:1531px;width:541px;height:449px;background:radial-gradient(ellipse at 55% 60%,#7a0f1c,#20121f 55%,#0b0d1a)"></div>
</section>

<section class="hardware">
  <div class="abs media" role="img" aria-label="Patient resting an arm on the imaging robot beside a window looking out on Earth"
       style="left:58px;top:2195px;width:540px;height:406px;background:linear-gradient(150deg,#1d3b52,#5c7f93 45%,#d8dde4)"></div>
  <div class="pill" style="left:667px;top:2195px;width:126px">Product</div>
  <h2 class="abs section-title" style="left:666px;top:2243px">Hardware</h2>
  <p class="abs section-lede" style="left:667px;top:2356px;width:480px">Automating ultrasound to deliver consistent diagnostics.&nbsp;&nbsp;Fast.</p>
  <p class="abs section-body" style="left:667px;top:2451px;width:420px">The patient rests their arm or leg on the imaging robot throughout the scan, which begins at the push of a button.</p>
  <a class="btn" style="left:667px;top:2565px;width:180px;height:37px">Learn More
    <svg viewBox="0 0 14 14"><path d="M2 12 L12 2 M5 2 H12 V9" stroke="#fff" stroke-width="1.5" fill="none"/></svg></a>
</section>

<section class="abs cta" style="left:54px;top:2763px;width:1088px;height:230px;border-radius:10px;background:linear-gradient(160deg,#9106d6 0%,#c10bb8 45%,#f01b85 80%,#f4616a 100%)">
  <p class="abs" style="left:177px;top:48px;width:760px;color:#fff;font-size:29px;font-weight:700;line-height:37px;letter-spacing:-.3px">Tralom is building the next generation of non-invasive medical imaging and intelligent patient monitoring.</p>
  <a class="btn" style="left:468px;top:153px;width:154px;height:36px">Contact
    <svg viewBox="0 0 14 14"><path d="M2 12 L12 2 M5 2 H12 V9" stroke="#fff" stroke-width="1.5" fill="none"/></svg></a>
</section>

<footer class="site-footer">
  <div class="abs brand" style="left:60px;top:3108px;font-size:44px;line-height:50px">Tralom</div>
  <nav class="nav" style="font-size:14px;font-weight:500">
    <a style="left:431px;top:3125px">Home</a>
    <a style="left:509px;top:3125px">About</a>
    <a style="left:588px;top:3125px">Technology</a>
    <a style="left:705px;top:3125px">Work with us</a>
    <a style="left:825px;top:3125px">Contact</a>
  </nav>
  <a class="abs" style="right:58px;top:3125px;font-size:14px;font-weight:500;color:var(--ink);text-decoration:none">info@tralom.com</a>
  <div class="abs" style="left:0;top:3184px;width:1200px;height:1px;background:var(--rule)"></div>
  <p class="abs" style="left:58px;top:3200px;font-size:12px">© 2025 TRALOM PTY LTD</p>
  <p class="abs" style="left:480px;top:3200px;font-size:12px">For use by qualified healthcare professionals only.</p>
  <p class="abs" style="right:58px;top:3200px;font-size:12px">Privacy policy</p>
</footer>

</body>
</html>
```